Building Company Business Card Design

Need a design for a business card:
It needs to have: Name, Phone, Facebook link, Website, email
i would also like a list of works we undertake:
-New Homes
-Extensions, Renovations & Bathrooms
-Decking, Carports, Sheds (Residential and Industrial)
-Carpentry
-Fences, Patios & Pergolas

Name, Phone, Facebook link, Website, email + details of services provided listed in description

```html
<!DOCTYPE html>
<html lang="en">
<head>
<meta charset="utf-8">
<title>Cedarline Homes – Business Card</title>
<link rel="stylesheet" href="https://fonts.googleapis.com/css2?family=Montserrat:wght@400;500;600&family=Exo+2:wght@600&display=swap">
<style>
  :root {
    --bg: #a2a2a2;
    --white: #ffffff;
    --ink: #1a1a1a;
    --black: #000000;
    --card-dark: #08090b;
    --green: #33b44a;
  }
  * { margin: 0; padding: 0; box-sizing: border-box; }
  html, body { width: 1093px; height: 1200px; overflow: hidden; }
  body { background: var(--bg); font-family: "Montserrat", sans-serif; position: relative; }

  .card {
    position: absolute; left: 265px; width: 595px; height: 363px;
    border-radius: 22px; overflow: hidden;
  }
  .card--front { top: 225px; background: var(--white); }
  .card--back { top: 615px; background: var(--card-dark); color: var(--white); }

  .front__swoosh { position: absolute; left: 0; top: 0; width: 595px; height: 363px; }

  .brand {
    position: absolute; display: flex; align-items: center; gap: 8px;
    font-weight: 600; text-transform: uppercase; white-space: nowrap;
  }
  .brand__mark { background: var(--green); flex: none; }
  .card--front .brand {
    left: 60px; width: 220px; top: 188px; justify-content: center;
    font-size: 16px; color: var(--ink); letter-spacing: 0.3px; gap: 7px;
  }
  .card--front .brand__mark { width: 12px; height: 12px; }

  .divider { position: absolute; left: 297px; top: 124px; width: 1.5px; height: 142px; background: var(--green); }

  .person { position: absolute; left: 309px; top: 120px; }
  .person__name { font-family: "Exo 2", sans-serif; font-weight: 600; font-size: 24px; color: var(--green); line-height: 1; }
  .person__title { font-size: 14px; color: var(--ink); margin-top: 6px; }

  .contacts { position: absolute; left: 309px; top: 178px; list-style: none; }
  .contacts li { display: flex; align-items: center; gap: 7px; height: 23.5px; font-size: 14px; color: var(--ink); }
  .contacts svg { width: 13px; height: 13px; flex: none; }

  .card--back .brand { left: 0; right: 0; top: 130px; justify-content: center; font-size: 30px; color: var(--white); letter-spacing: 1px; gap: 12px; }
  .card--back .brand__mark { width: 22px; height: 22px; }

  .services { position: absolute; left: 0; right: 0; top: 220px; text-align: center; }
  .services__title {
    display: inline-block; font-size: 16px; font-weight: 500; color: var(--green);
    padding: 0 4px 4px; border-bottom: 1.5px solid var(--white);
  }
  .services__list { margin-top: 12px; font-size: 13.5px; font-weight: 500; line-height: 25px; }
  .services__item::before {
    content: ""; display: inline-block; width: 5px; height: 5px; border-radius: 50%;
    background: var(--green); margin: 0 5px 2px 5px; vertical-align: middle;
  }
</style>
</head>
<body>

<section class="card card--front">
  <svg class="front__swoosh" viewBox="0 0 595 363" aria-hidden="true">
    <path d="M0,288 C180,330 420,330 595,262 V363 H0 Z" fill="var(--green)"/>
    <path d="M0,288 C180,336 420,338 595,288 V363 H0 Z" fill="var(--black)"/>
  </svg>

  <div class="brand"><span class="brand__mark"></span>Cedarline Homes</div>

  <div class="divider"></div>

  <div class="person">
    <p class="person__name">Daniel Brooks</p>
    <p class="person__title">Managing Director</p>
  </div>

  <ul class="contacts">
    <li>
      <svg viewBox="0 0 24 24"><path fill="var(--green)" d="M6.6 10.8a15 15 0 0 0 6.6 6.6l2.2-2.2a1 1 0 0 1 1-.25 11.4 11.4 0 0 0 3.6.57 1 1 0 0 1 1 1V20a1 1 0 0 1-1 1A17 17 0 0 1 3 4a1 1 0 0 1 1-1h3.5a1 1 0 0 1 1 1c0 1.25.2 2.450.57 3.57a1 1 0 0 1-.25 1Z"/></svg>
      555-318-0427
    </li>
    <li>
      <svg viewBox="0 0 24 24"><rect x="2" y="5" width="20" height="14" rx="1.5" fill="var(--green)"/><path d="M3 6l9 7 9-7" stroke="var(--white)" stroke-width="1.8" fill="none"/></svg>
      info@cedarlinehomes.com
    </li>
    <li>
      <svg viewBox="0 0 24 24"><circle cx="12" cy="12" r="10" fill="var(--green)"/><path d="M2 12h20M12 2c3 3 3 17 0 20M12 2c-3 3-3 17 0 20" stroke="var(--white)" stroke-width="1.4" fill="none"/></svg>
      www.cedarlinehomes.com
    </li>
    <li>
      <svg viewBox="0 0 24 24"><circle cx="12" cy="12" r="11" fill="var(--green)"/></svg>
      www.social.com/cedarlinehomes
    </li>
  </ul>
</section>

<section class="card card--back">
  <div class="brand"><span class="brand__mark"></span>Cedarline Homes</div>

  <div class="services">
    <h2 class="services__title">Our Services</h2>
    <div class="services__list">
      <p><span class="services__item">New Homes</span> <span class="services__item">Extensions, Renovations &amp; Bathrooms</span></p>
      <p><span class="services__item">Decking, Carports, Sheds (Residential and Industrial)</span></p>
      <p><span class="services__item">Carpentry</span> <span class="services__item">Fences, Patios &amp; Pergolas</span></p>
    </div>
  </div>
</section>

</body>
</html>
```